Mandala Postcard Design

I am in need of a postcard to hand out at a Psychic Fair. I envision the card to having half-of-a Mandala (from my Facebook folder), touched up a bit to make it vibrant and bold. Others vendors will have cards w/photographic backgrounds doing yoga. I'd like mine to stand out for it's line-drawn "cartoonish" nature, solid-color nature. The wording would be my basic contact info and a short description ... something like: "Experience the Magic of Mandala Making ... Next Class will be held: (open space for writing, no lines) The art is contained in this Facebook folder. Lots to choose from, with my favorites being the stronger outlined designs.

https://www.sketchnook.example/Brightloom/media_set?set=a.20262926615637197.2184852941.783542196&type=3
Updates

I just uploaded a few new drawings that might work better, since they are more round. I want to minimize the white space, for instance, avoid having the left & right corners empty. Another idea could be to use 1/4 mandalas in the corners. I'm ready to make a decision. I want it to look great, but as I gain drawing experience, I'll need to update my cards. Thanks! I'm not sure if this the place for this comment, but I'll also be needing a DVD label for my tutorials, and a front page design for a mandala coloring book.

Target Market(s)

Primarily women interested in metaphysical, psychic, meditation, reiki and a basic interest in art.

Font styles to use
Serif
Sans Serif

Requirements
Should not have
• Should not be on a dark card, really should be a plain white background, it seems, in order to stand out.

```html
<!DOCTYPE html>
<html lang="en">
<head>
<meta charset="utf-8">
<title>Experience the Magic of Mandala Making</title>
<link rel="stylesheet" href="https://fonts.googleapis.com/css2?family=Limelight&family=Archivo:wght@800&display=swap">
<style>
  :root {
    --paper: #ffffff;
    --ink: #000000;
    --rose: #f0306f;
    --magenta: #c2268f;
    --orchid: #ee88e8;
    --lime: #93f53e;
    --turquoise: #4de8d8;
    --slot-fill: #d6d6d6;
    --slot-edge: #a9a9a9;
    --mandala-core: #f4a07a;
    --mandala-mid: #3ec9c4;
    --mandala-outer: #e8348f;
    --mandala-rim: #f2efe8;
  }
  html, body {
    margin: 0;
    padding: 0;
    overflow: hidden;
    background: var(--paper);
  }
  .postcard {
    position: relative;
    width: 1200px;
    height: 949px;
    background: var(--paper);
    overflow: hidden;
  }
  .mandala-art {
    position: absolute;
    left: 234px;
    top: 230px;
    width: 542px;
    height: 546px;
    overflow: hidden;
  }
  .mandala-art__disc {
    position: absolute;
    left: -200px;
    top: -108px;
    width: 740px;
    height: 740px;
    border-radius: 50%;
    background: radial-gradient(circle,
      var(--mandala-core) 0%,
      var(--mandala-core) 14%,
      var(--mandala-mid) 22%,
      #d98be0 30%,
      #b9e83a 45%,
      var(--mandala-outer) 62%,
      #f0a070 72%,
      var(--mandala-rim) 80%,
      var(--mandala-rim) 92%,
      #e0409a 96%);
    box-shadow: 8px 10px 18px rgba(0,0,0,0.35);
  }
  .headline {
    position: absolute;
    left: 772px;
    top: 308px;
    width: 420px;
    margin: 0;
    font-family: "Limelight", serif;
    font-weight: 400;
    text-align: center;
    line-height: 1;
  }
  .headline span {
    display: block;
    text-shadow: -1px -1px 0 var(--ink), 1px -1px 0 var(--ink), -1px 1px 0 var(--ink), 5px 5px 0 var(--ink);
  }
  .headline__experience { color: var(--rose); font-size: 68px; }
  .headline__magic { color: var(--magenta); font-size: 68px; margin-top: 4px; }
  .headline__of { color: var(--orchid); font-size: 80px; margin-top: 0; }
  .headline__mandala { color: var(--lime); font-size: 76px; margin-top: 2px; }
  .headline__making { color: var(--turquoise); font-size: 104px; margin-top: -12px; }
  .next-class {
    position: absolute;
    left: 293px;
    top: 840px;
    margin: 0;
    font-family: "Archivo", sans-serif;
    font-weight: 800;
    font-size: 24px;
    color: var(--ink);
  }
  .next-class__slot {
    position: absolute;
    left: 281px;
    top: 875px;
    width: 564px;
    height: 59px;
    background: var(--slot-fill);
    border: 1px solid var(--slot-edge);
    border-radius: 14px;
  }
</style>
</head>
<body>
  <main class="postcard">
    <div class="mandala-art" role="img" aria-label="Hand-drawn colourful half mandala with a peach flower centre and pink, lime and turquoise petals">
      <div class="mandala-art__disc"></div>
    </div>
    <h1 class="headline">
      <span class="headline__experience">Experience</span>
      <span class="headline__magic">the Magic</span>
      <span class="headline__of">of</span>
      <span class="headline__mandala">Mandala</span>
      <span class="headline__making">Making</span>
    </h1>
    <p class="next-class">Next Class will be held</p>
    <div class="next-class__slot"></div>
  </main>
</body>
</html>
```